4 Widows HAUNTED Beyond Dusk (A household sinking under ancient vows)

I want my book cover to coincide with the title. The "T" In Birth I want to be a cross with God on it. I want some of the letters melting. I also want a pit or a pool of fire with 9 fiery sisters drowning in it. It doesn't necessarily have to show the complete body, it can partial, some full, and some with just the hands coming out the fire like they have already drowned. The color of the cover I rather have it black since the fire is reddish, yellow/orange; but I'm open to creativity. My book should look like the place "Hell" since that's what my non-fiction book is all about. It's a true story of a struggling family living the hard knock life in New York with a vulnerable mother without our father in our lives. We experienced living in and out of shelter, getting picked on everywhere we went, school dropouts, young teen pregnancies, victims of rape, abuse, drug use, had a lot of witchcraft interventions as well as some of us giving our lives to the devil. As we gotten old we became more evil, indulged in the 7 deadly sins was their daily routine which caused tragedies to the family and others, our family values is no longer valued, and we grew apart as a whole. So my book is delivering a message to all families who has similar stories. Inspirational to whoever is seeking guidance and understanding as well as a wake up call to struggling family, evildoers, and people who are trying to transition.. Also, I want to bring families back together; most definitely mine because we all have some sort of Envy, Greed, Lust, Rage, Sloth, Gluttony, Self-Pride, etc. Giving this brief description of my book, the cover should reveal strictly evil. No smiles, just sinful. On the back of my cover I will have a short description of my book, and telling a little about myself, so I can have a little fire on it to blend in with the front, but it's optional. I'm also open to creative ideas, so if you can make a cover through your experience that goes with my title, I am willing to see them. My book is already done and is waiting to be published so the cover is the only thing I am waiting on. I hope this information is helpful, and I'm hoping I can get a book cover I am looking for.

Font styles to use
Other font styles liked:
• I'm undecided

Colors

Designer to choose colors to be used in the design.

Requirements
Must have
• more than one person on the cover
Nice to have
• 9 fiery sisters drowning in a pool or pit of fire
Should not have
• one person on the cover

```html
<!DOCTYPE html>
<html lang="en">
<head>
<meta charset="utf-8">
<title>4 Widows Haunted Beyond Dusk — Cover Wrap</title>
<link rel="stylesheet" href="https://fonts.googleapis.com/css2?family=Cinzel:wght@400;700&family=Playfair+Display:wght@700;900&family=Montserrat:wght@400;500;600&family=Archivo:wght@600&display=swap">
<style>
  :root {
    --night: #000000;
    --ember-dark: #3a0300;
    --ember-red: #b80d02;
    --flame-red: #e3200b;
    --flame-orange: #f26a0c;
    --flame-gold: #f7b52a;
    --blurb-gold: #f2b02c;
    --ash-white: #f1ece6;
  }
  * { box-sizing: border-box; margin: 0; padding: 0; }
  html, body { width: 1200px; height: 843px; overflow: hidden; background: var(--night); }
  .cover-wrap { position: relative; width: 1200px; height: 843px; background: var(--night); overflow: hidden; }

  /* Back cover */
  .back-fire-scene {
    position: absolute; left: 170px; top: 0; width: 360px; height: 240px;
    background: radial-gradient(ellipse at 55% 40%, rgba(200,30,5,.85) 0%, rgba(120,10,0,.6) 40%, rgba(0,0,0,0) 75%);
  }
  .back-title { position: absolute; left: 0; top: 0; width: 600px; height: 230px; }
  .back-blurb {
    position: absolute; left: 48px; top: 230px; width: 474px;
    font-family: "Montserrat", sans-serif; font-size: 9.6px; line-height: 13.9px;
    color: var(--blurb-gold); text-align: left;
  }
  .back-blurb p { margin: 0; }
  .back-ground-fire {
    position: absolute; left: 0; top: 584px; width: 560px; height: 150px;
    background: linear-gradient(180deg, #c9220e 0%, #8e1306 45%, #3a0502 80%, rgba(0,0,0,0) 100%);
    border-radius: 6px 30px 0 0;
  }

  /* Spine */
  .spine-numeral {
    position: absolute; left: 578px; top: 82px; width: 36px; text-align: center;
    font-family: "Playfair Display", serif; font-weight: 900; font-size: 40px;
    color: var(--flame-orange); transform: rotate(90deg);
  }
  .spine-title {
    position: absolute; left: 576px; top: 130px; height: 470px;
    writing-mode: vertical-rl;
    font-family: "Cinzel", serif; font-weight: 400; font-size: 27px; letter-spacing: 0.5px;
    color: var(--flame-orange); white-space: nowrap;
  }
  .spine-author {
    position: absolute; left: 588px; top: 632px; height: 170px;
    writing-mode: vertical-rl;
    font-family: "Montserrat", sans-serif; font-weight: 500; font-size: 13px; letter-spacing: 6px;
    color: var(--flame-gold); white-space: nowrap;
  }

  /* Front cover */
  .front-tagline {
    position: absolute; left: 640px; top: 34px; width: 560px; text-align: center;
    font-family: "Cinzel", serif; font-weight: 400; font-size: 18px; letter-spacing: 0.6px;
    color: var(--flame-gold);
  }
  .front-title { position: absolute; left: 612px; top: 50px; width: 588px; height: 430px; }
  .front-fire-pit {
    position: absolute; left: 640px; top: 480px; width: 520px; height: 250px;
    background: radial-gradient(ellipse at 50% 50%, #ffd34d 0%, #f7891a 28%, #d8300a 55%, rgba(120,10,0,.5) 75%, rgba(0,0,0,0) 100%);
  }
  .front-author {
    position: absolute; left: 612px; top: 776px; width: 588px; text-align: center;
    font-family: "Montserrat", sans-serif; font-weight: 500; font-size: 25px; letter-spacing: 13px;
    color: var(--ash-white);
  }
</style>
</head>
<body>
<main class="cover-wrap">

  <section class="back-cover">
    <div class="back-fire-scene" role="img" aria-label="Dark red burning forest at night"></div>
    <svg class="back-title" viewBox="0 0 600 230" aria-label="4 Widows">
      <defs>
        <linearGradient id="backNumeralFire" x1="0" y1="0" x2="0" y2="1">
          <stop offset="0" stop-color="#ffd36a"/>
          <stop offset=".5" stop-color="#f26a0c"/>
          <stop offset="1" stop-color="#b3150a"/>
        </linearGradient>
        <linearGradient id="backWordFire" x1="0" y1="0" x2="0" y2="1">
          <stop offset="0" stop-color="#f7b52a"/>
          <stop offset="1" stop-color="#e3200b"/>
        </linearGradient>
      </defs>
      <text x="272" y="200" text-anchor="middle" font-family="Playfair Display, serif" font-weight="900" font-size="190" fill="url(#backNumeralFire)" opacity=".55">4</text>
      <text x="295" y="146" text-anchor="middle" font-family="Playfair Display, serif" font-weight="700" font-size="44" fill="url(#backWordFire)" stroke="#2a0200" stroke-width="1.5" paint-order="stroke">WIDOWS</text>
    </svg>

    <div class="back-blurb">
      <p>4 widows haunted beyond dusk is about Odessa Graywell, who was a single mother struggling to raise 4 kids in the hard knock life of New York. She practically had no one to turn to because her husband consistently deceived, depressed, devalued, and then deserted her. Her sisters were resentful, and her brothers were barbaric; however, the most hurtful part of it all was that she didn't have a father, and her mother Marguerite despised everything about her. She didn't give Odessa that motherly love, them motherly kisses, nor did she hold her hands through all those dark places. The bottom line is that Marguerite faltered and failed as a parent.</p>
      <p>For those reasons, Odessa didn't have the fuel that empowered her to do the impossible because she was naïve, vulnerable, and lost in this cruel world, until she found God. But when she became so caught up in her religious life, she didn't realize that her kids were feeling less important. They had no father, barely had a mother, and they were very disturbed about being the unfortunate kids on the block; therefore, they all begin to gradually change. The 4 girls' unstable life had triggered the inherited evil blood that was flowing within them, which had a huge impact on their behavior.</p>
      <p>That's when the family begin to unravel because the 7 deadly sins had taken control over their souls. "Anger" conquered us all because we were bitter about the lives we were given; For that reason, "Greed" defeated us since we desired what we never had and would do anything to get what we wanted. Some of our weaknesses was "Slothfulness," for we didn't work hard towards progression due to our persistent ignorance and disadvantages. Yet, "Envy" played a huge role towards the sisters who made achievements, but in this family, "Pride" won't let them acknowledge one's accomplishments; instead, "Gluttony" caused some of them to "Lust" over and try to destroy what the other sister have because they wanted to feel loved and equally important. These Challenges stand strong in our family, and the only way to subjugate our sins relies strictly within ourselves. So can our curse be reversed? Or, will it continue to condemn our bloodline, our appearance, and the unity in our family?</p>
    </div>

    <div class="back-ground-fire" role="img" aria-label="Red ground with small fires burning and a figure lying among the flames"></div>
  </section>

  <section class="spine">
    <div class="spine-numeral">4</div>
    <div class="spine-title">WIDOWS HAUNTED BEYOND DUSK</div>
    <div class="spine-author">MARISOL VANE</div>
  </section>

  <section class="front-cover">
    <div class="front-tagline">A Household Sinking Under Ancient Vows</div>

    <svg class="front-title" viewBox="0 0 588 430" aria-label="4 Widows Haunted Beyond Dusk">
      <defs>
        <linearGradient id="numeralFire" x1="0" y1="0" x2="0" y2="1">
          <stop offset="0" stop-color="#ffe08a"/>
          <stop offset=".45" stop-color="#f58a1f"/>
          <stop offset="1" stop-color="#c2250a"/>
        </linearGradient>
        <linearGradient id="redWord" x1="0" y1="0" x2="0" y2="1">
          <stop offset="0" stop-color="#ff3b1a"/>
          <stop offset="1" stop-color="#b80d02"/>
        </linearGradient>
        <linearGradient id="hauntedWord" x1="0" y1="0" x2="0" y2="1">
          <stop offset="0" stop-color="#ff2a10"/>
          <stop offset=".6" stop-color="#ee4a10"/>
          <stop offset="1" stop-color="#f28a1a"/>
        </linearGradient>
        <linearGradient id="duskWord" x1="0" y1="0" x2="0" y2="1">
          <stop offset="0" stop-color="#f7c12e"/>
          <stop offset=".55" stop-color="#f37d12"/>
          <stop offset="1" stop-color="#e3200b"/>
        </linearGradient>
      </defs>
      <text class="title-numeral" x="138" y="158" text-anchor="middle" font-family="Playfair Display, serif" font-weight="900" font-size="170" fill="url(#numeralFire)">4</text>
      <text x="212" y="134" font-family="Playfair Display, serif" font-weight="900" font-size="72" fill="url(#redWord)" textLength="312" lengthAdjust="spacingAndGlyphs">WIDOWS</text>
      <text x="68" y="262" font-family="Playfair Display, serif" font-weight="900" font-size="118" fill="url(#hauntedWord)" textLength="464" lengthAdjust="spacingAndGlyphs">HAUNTED</text>
      <text x="192" y="326" font-family="Playfair Display, serif" font-weight="900" font-size="58" fill="url(#redWord)" textLength="216" lengthAdjust="spacingAndGlyphs">BEYOND</text>
      <rect x="248" y="358" width="5" height="40" fill="#c0150a"/>
      <rect x="332" y="358" width="4" height="54" fill="#c0150a"/>
      <text x="148" y="420" font-family="Archivo, sans-serif" font-weight="600" font-size="92" fill="url(#duskWord)" textLength="320" lengthAdjust="spacingAndGlyphs">DUSK</text>
    </svg>

    <div class="front-fire-pit" role="img" aria-label="Pit of fire with several women drowning in the flames, some with only their hands rising out"></div>

    <div class="front-author">MARISOL VANE</div>
  </section>

</main>
</body>
</html>
```